adult dating promotion banners

target website: plomkaverling.nl
i need multiple good banner for an add campaign on quillmo.net
no male images in the banner, onlygirls
animatedly: yes
sizes: 300x250px and 728x110px

Target Market(s)

dutch guys looking for an date

Industry/Entity Type

dating

Requirements
Must have
• striking pictures
Nice to have
• free signup 2 free credits
Should not have
• no male images

```html
<!DOCTYPE html>
<html lang="nl">
<head>
<meta charset="utf-8">
<title>plomkaverling.nl banners</title>
<link href="https://fonts.googleapis.com/css2?family=Roboto:wght@300;400;500&display=swap" rel="stylesheet">
<style>
  :root {
    --red: #ff0000;
    --orange: #ff9900;
    --ink: #222222;
    --white: #ffffff;
    --border: #333333;
    --tone-warm: #c89a7c;
    --tone-dark: #3a2a22;
    --tone-light: #f1ece8;
    --btn-blue: #0a7cff;
    --btn-green: #28a745;
    --btn-yellow: #ffc107;
    --btn-bar: #fff3c4;
  }
  * { box-sizing: border-box; margin: 0; padding: 0; }
  html, body { width: 1200px; height: 800px; overflow: hidden; background: var(--white); }
  body { position: relative; font-family: "Roboto", Arial, sans-serif; }

  .banner { position: absolute; overflow: hidden; border: 1px solid var(--border); }
  .banner--square { width: 242px; height: 202px; top: 136px; }
  .banner--wide { width: 584px; height: 90px; left: 98px; }

  .photo { position: absolute; inset: 0; }
  .photo--warm { background: linear-gradient(135deg, #f4f0ee 0%, #d9b49a 40%, #2b2b2b 70%, #e6d2c6 100%); }
  .photo--bed { background: linear-gradient(160deg, #3c2a20 0%, #b98466 35%, #e8dcd6 70%, #ffffff 100%); }
  .photo--bright { background: linear-gradient(180deg, #a97a5b 0%, #c89272 45%, #d6f243 60%, #b07c5c 100%); }
  .photo--dusk { background: linear-gradient(90deg, #4a382e 0%, #a47c62 35%, #6b5040 60%, #3a2a22 100%); }
  .photo--lace { background: linear-gradient(90deg, #2a2220 0%, #b48a74 35%, #d9c6bb 60%, #ffffff 72%); }
  .photo--room { background: linear-gradient(90deg, #5d4a3e 0%, #8e6a52 35%, #6a5040 60%, #3a2a22 100%); }

  .band { position: absolute; inset: 0; width: 100%; height: 100%; }

  .domain { position: absolute; color: var(--white); font-weight: 500; white-space: nowrap; }
  .tagline { position: absolute; white-space: nowrap; }

  .square-domain { left: 0; right: 0; bottom: 4px; text-align: center; font-size: 22px; }

  .fade-bottom { position: absolute; left: 0; right: 0; bottom: 0; height: 60px;
    background: linear-gradient(180deg, rgba(255,255,255,0) 0%, rgba(250,240,234,0.95) 40%, #fbf3ee 100%); }
  .square-light .tagline { left: 0; right: 0; top: 149px; text-align: center; font-size: 17.5px; color: var(--ink); }
  .square-light .domain { left: 0; right: 0; top: 170px; text-align: center; font-size: 22.5px; color: var(--red); font-weight: 400; }

  .wide-red .tagline { left: 315px; width: 212px; top: 17px; text-align: center; font-size: 22px; font-weight: 300; color: var(--white); }
  .wide-red .domain { left: 266px; width: 300px; top: 43px; text-align: center; font-size: 35.5px; }

  .wide-light .button-bar { position: absolute; left: 318px; top: 3px; width: 242px; height: 34px;
    background: var(--btn-bar); display: flex; align-items: center; justify-content: space-evenly; }
  .btn { font-size: 9.5px; color: var(--white); border-radius: 2px; padding: 5px 7px; line-height: 1; }
  .btn--signup { background: var(--btn-blue); }
  .btn--login { background: var(--btn-green); }
  .btn--request { background: var(--btn-yellow); color: var(--ink); }
  .wide-light .tagline { left: 318px; width: 242px; top: 35px; text-align: center; font-size: 17.5px; color: var(--ink); }
  .wide-light .domain { left: 315px; width: 250px; top: 50px; text-align: center; font-size: 29px; color: var(--red); font-weight: 400; }
</style>
</head>
<body>

  <div class="banner banner--square square-red" style="left:98px">
    <div class="photo photo--warm" role="img" aria-label="Vrouw in zwarte lingerie liggend op wit laken"></div>
    <svg class="band" viewBox="0 0 242 202" preserveAspectRatio="none" aria-hidden="true">
      <path d="M0 166 Q150 160 242 122 L242 202 L0 202 Z" fill="var(--orange)"/>
      <path d="M0 170 Q160 166 242 132 L242 202 L0 202 Z" fill="var(--red)"/>
    </svg>
    <div class="domain square-domain">plomkaverling.nl</div>
  </div>

  <div class="banner banner--square square-light" style="left:389px">
    <div class="photo photo--bed" role="img" aria-label="Vrouw in lingerie en kousen op bed, van achteren gezien"></div>
    <div class="fade-bottom"></div>
    <div class="tagline">Chat direct anoniem!</div>
    <div class="domain">plomkaverling.nl</div>
  </div>

  <div class="banner banner--square square-red" style="left:680px">
    <div class="photo photo--bright" role="img" aria-label="Vrouw in neongele bikini met halsketting"></div>
    <svg class="band" viewBox="0 0 242 202" preserveAspectRatio="none" aria-hidden="true">
      <path d="M0 166 Q150 160 242 122 L242 202 L0 202 Z" fill="var(--orange)"/>
      <path d="M0 170 Q160 166 242 132 L242 202 L0 202 Z" fill="var(--red)"/>
    </svg>
    <div class="domain square-domain">plomkaverling.nl</div>
  </div>

  <div class="banner banner--wide wide-red" style="top:386px">
    <div class="photo photo--dusk" role="img" aria-label="Liggende vrouw in zwarte bh"></div>
    <svg class="band" viewBox="0 0 584 90" preserveAspectRatio="none" aria-hidden="true">
      <path d="M192 90 Q270 80 292 0 L584 0 L584 90 Z" fill="var(--red)"/>
    </svg>
    <div class="tagline">Chat direct anoniem!</div>
    <div class="domain">plomkaverling.nl</div>
  </div>

  <div class="banner banner--wide wide-light" style="top:513px">
    <div class="photo photo--lace" role="img" aria-label="Vrouw met kanten masker, liggend"></div>
    <div class="button-bar">
      <span class="btn btn--signup">Gratis inschrijven</span>
      <span class="btn btn--login">Inloggen</span>
      <span class="btn btn--request">Opvragen</span>
    </div>
    <div class="tagline">Chat direct anoniem!</div>
    <div class="domain">plomkaverling.nl</div>
  </div>

  <div class="banner banner--wide wide-red" style="top:646px">
    <div class="photo photo--room" role="img" aria-label="Vrouw in lingerie geknield in slaapkamer"></div>
    <svg class="band" viewBox="0 0 584 90" preserveAspectRatio="none" aria-hidden="true">
      <path d="M192 90 Q270 80 292 0 L584 0 L584 90 Z" fill="var(--red)"/>
    </svg>
    <div class="tagline">Chat direct anoniem!</div>
    <div class="domain">plomkaverling.nl</div>
  </div>

</body>
</html>
```